Creating a website for a life changing company (Vantara Q)

We do need a website for our Coaching and Consulting business we recently launched. We do need it for information purposes and that our clients do have the opportunity to subscribe for packages, programs etc.
We would like to see designs which use the colours blue and yellow (see attachment). The final design should communicate our passion for the potential in people and the benefit (going beyond) for them.
Updates
Additional information:
Our company (webpage): Vantara Q (the C stands for "what people cannot see / imagine now...)
Welcome to Vantara Q(uest)
Consulting (O.R.B.) & Coaching (Rise onward)
Two pillars:
1) O.R.B. ( Leadership evolution - Our program - focussing on companies - business orientated)
2) Rise onward (Life transformation - Events - focusing on individuals - primarily life changing)
For both of them we offer: Concierge & Vantara Q+ (This should go as a subscription)
Eventually you can draft this as a rhombus
Industry/Entity Type
Coaching / Consulting
Coding
Coded - Design and coding required
Number of Pages Required
1 page
Font styles to use
Other font styles liked:
- Lato
Requirements
Must have
- Please see attachment (About us / Offers / Calendar function / Links to Instagram and LinkedIn account / mailing list / page for clients
Nice to have
- A banner

```html
<!DOCTYPE html>
<html lang="en">
<head>
<meta charset="utf-8">
<title>Vantara Q — Life Changing Center</title>
<link href="https://fonts.googleapis.com/css2?family=Lato:wght@400;700;900&display=swap" rel="stylesheet">
<style>
:root{
  --blue:#0a4fb0;
  --blue-bright:#1268d8;
  --blue-deep:#0a3f9a;
  --yellow:#f8cf3f;
  --yellow-soft:#fbeec0;
  --ink:#111827;
  --text:#4a4f5a;
  --white:#ffffff;
  --line:#e4e6ea;
}
*{box-sizing:border-box;margin:0;padding:0}
html,body{width:1200px;height:4910px;overflow:hidden;background:var(--white)}
body{font-family:'Lato',sans-serif;color:var(--ink)}
.page{position:relative;width:1200px;height:4910px;overflow:hidden}
.abs{position:absolute}
a{text-decoration:none;color:inherit}

/* header */
.site-header{position:absolute;left:0;top:0;width:1200px;height:149px;background:var(--white);border-top:3px solid var(--blue)}
.brand{position:absolute;display:flex;align-items:center;gap:8px;font-weight:700;letter-spacing:3px}
.brand-dot{width:34px;height:34px;border-radius:50%;background:var(--yellow)}
.header-brand{left:114px;top:70px;color:var(--blue);font-size:15px}
.main-nav{position:absolute;left:263px;top:80px;display:flex;gap:32px;font-size:13px;font-weight:900}
.phone-pill{position:absolute;left:900px;top:0;width:186px;height:38px;background:var(--blue);color:var(--white);border-radius:0 0 12px 12px;display:flex;align-items:center;justify-content:center;gap:8px;font-size:15px}
.btn{display:flex;align-items:center;justify-content:center;border-radius:20px;font-weight:900;position:absolute}
.btn-contact{left:950px;top:69px;width:136px;height:38px;background:var(--yellow);font-size:14px}

/* hero */
.hero{position:absolute;left:0;top:149px;width:1200px;height:708px;background:linear-gradient(100deg,#1d2f22 0%,#35503a 35%,#27412e 60%,#4d6a48 85%,#8a9a6a 100%)}
.hero-title{position:absolute;right:114px;top:195px;text-align:right;color:var(--white);font-weight:900;font-size:56px;line-height:76px;letter-spacing:-1px}
.hero-sub{position:absolute;right:114px;top:355px;width:600px;text-align:right;color:var(--white);font-weight:700;font-size:17px;line-height:24px}
.btn-hero{left:931px;top:443px;width:155px;height:37px;background:var(--white);color:var(--blue);font-size:17px}

/* section headings */
.heading{position:absolute;display:flex;align-items:center;gap:14px;font-weight:900;font-size:32px;letter-spacing:-0.5px}
.heading-dot{width:44px;height:44px;border-radius:50%;background:var(--yellow)}
.heading.center{left:0;width:1200px;justify-content:center}

.copy{position:absolute;font-size:14px;line-height:21px;color:var(--text)}
.copy p+p{margin-top:20px}
.btn-blue{background:var(--blue);color:var(--white);font-size:16px;height:37px}

.portrait-ring{position:absolute;border-radius:50%;background:var(--yellow-soft)}
.portrait{position:absolute;border-radius:50%}

/* concierge */
.concierge{position:absolute;left:0;top:1977px;width:1200px;height:709px;background:linear-gradient(160deg,var(--blue-bright) 0%,#1a73e0 45%,var(--blue-deep) 100%)}
.concierge-lead{position:absolute;left:0;top:190px;width:1200px;text-align:center;color:var(--white);font-size:15px}
.service{position:absolute;width:210px;text-align:center;color:var(--white);font-weight:700;font-size:15px}
.service-photo{width:210px;height:210px;border-radius:50%;border:5px solid var(--yellow);margin-bottom:22px}

/* plans */
.plan{position:absolute;top:2833px;width:276px;height:272px;background:var(--white);box-shadow:0 0 6px rgba(0,0,0,.12);text-align:center}
.plan-icon{position:absolute;left:104px;top:-34px;width:68px;height:68px;border-radius:50%;background:var(--blue);border:3px solid #dbe6f7}
.plan h3{margin-top:52px;font-size:15px;font-weight:700}
.plan-text{margin:14px auto 0;width:246px;font-size:12px;line-height:18px;color:var(--text)}
.plan ul{list-style:none;margin:10px 0 0 34px;text-align:left;font-size:12px;color:var(--text)}
.plan li{display:flex;align-items:center;gap:10px;height:26px}
.plan .btn{left:76px;bottom:-15px;width:124px;height:37px}

/* plus */
.plus{position:absolute;left:0;top:3166px;width:1200px;height:726px;background:linear-gradient(180deg,#e9be2e 0%,#f6cd44 50%,#f9d453 100%)}
.plus-card{position:absolute;top:3492px;width:313px;text-align:center}
.plus-photo{height:194px;border:4px solid var(--white)}
.plus-card h3{margin-top:27px;font-size:18px;font-weight:900}
.plus-card p{margin:8px auto 0;width:290px;font-size:12px;line-height:18px}
.btn-white{position:relative;margin:16px auto 0;width:124px;height:35px;background:var(--white);font-size:16px;display:flex}

/* contact */
.contact-item{position:absolute;left:166px;display:flex;gap:18px}
.contact-item h4{font-size:17px;font-weight:700;color:var(--ink)}
.contact-item p{font-size:12px;line-height:17px;color:var(--text);margin-top:6px}
.form-box{position:absolute;left:543px;top:4107px;width:543px;height:313px;background:var(--white);box-shadow:0 0 6px rgba(0,0,0,.12)}
.field{position:absolute;height:26px;border-bottom:1px solid #9aa0a8;font-size:12px;color:var(--text)}
.btn-submit{left:378px;top:229px;width:124px;height:37px}

/* footer */
.footer-nav{position:absolute;left:0;top:4748px;width:1200px;display:flex;justify-content:center;gap:44px;color:var(--white);font-size:13px;font-weight:900}
.footer-rule{position:absolute;left:114px;top:4806px;width:972px;height:1px;background:#3a3a3a}
.copyright{position:absolute;left:232px;top:4856px;color:var(--white);font-size:11px}
.socials{position:absolute;left:838px;top:4849px;display:flex;gap:8px}
.socials span{width:26px;height:26px;border-radius:50%;background:var(--white);border:4px solid var(--blue)}
</style>
</head>
<body>
<div class="page">

  <!-- Header -->
  <header class="site-header">
    <a class="brand header-brand" href="#"><span class="brand-dot"></span>VANTARA Q</a>
    <nav class="main-nav">
      <a href="#">HOME</a><a href="#">ABOUT US</a><a href="#">O.R.B.</a><a href="#">CONCIERGE</a><a href="#">RISE ONWARD</a><a href="#">VANTARA Q+</a><a href="#">TESTIMONIALS</a>
    </nav>
    <div class="phone-pill">
      <svg width="14" height="14" viewBox="0 0 24 24"><path fill="#fff" d="M6.6 10.8a15.1 15.1 0 0 0 6.6 6.6l2.2-2.2a1 1 0 0 1 1-.25 11.4 11.4 0 0 0 3.6.57 1 1 0 0 1 1 1V20a1 1 0 0 1-1 1A17 17 0 0 1 3 4a1 1 0 0 1 1-1h3.5a1 1 0 0 1 1 1c0 1.25.2 2.45.57 3.57a1 1 0 0 1-.25 1z"/></svg>
      (555) 010-4821
    </div>
    <a class="btn btn-contact" href="#">CONTACT US</a>
  </header>

  <!-- Hero -->
  <section class="hero" role="img" aria-label="Photo of a smiling woman on a zipline among forest trees">
    <h1 class="hero-title">WELCOME TO<br>LIFE CHANGING CENTER</h1>
    <p class="hero-sub">The Journey starts in the himalayas to Everest Base Camp, where transformation happened for both of them, it was going Vantara Q what they could see, comprehend and imagine.</p>
    <a class="btn btn-hero" href="#">Get Started</a>
  </section>
  <svg class="abs" style="left:0;top:690px" width="1200" height="170" viewBox="0 0 1200 170">
    <path d="M0 8 C200 110 520 150 1200 150 L1200 170 L0 170Z" fill="var(--blue)"/>
    <path d="M0 16 C200 118 520 156 1200 156 L1200 170 L0 170Z" fill="var(--yellow)"/>
    <path d="M0 22 C200 124 520 162 1200 162 L1200 170 L0 170Z" fill="#fff"/>
  </svg>

  <!-- About Mathis -->
  <h2 class="heading" style="left:118px;top:1001px"><span class="heading-dot"></span>ABOUT MATHIS</h2>
  <div class="copy" style="left:118px;top:1092px;width:500px">
    <p>I could tell you all about my facilitation and coaching experience, my degrees, and certificates. But none of that would tell you much about what matters most in working with me: the passion and support you will experience, the trust, the honesty, and the sense of growth and ease.</p>
    <p>The essence of my work is to facilitate self-growth by helping people identity the core challenges and setbacks in their lives so that they can overcome them with confidence. I call it "Living a passionate and cherish life"</p>
  </div>
  <a class="btn btn-blue" style="left:118px;top:1295px;width:181px" href="#">Connect With Us</a>
  <div class="portrait-ring" style="left:644px;top:932px;width:440px;height:440px"></div>
  <div class="portrait" style="left:665px;top:956px;width:396px;height:396px;background:linear-gradient(135deg,#b98a5c,#3d4f6e 55%,#1f2f55)" role="img" aria-label="Portrait of Mathis in a blue suit leaning on a railing"></div>

  <!-- About Lena -->
  <div class="portrait-ring" style="left:115px;top:1446px;width:440px;height:440px"></div>
  <div class="portrait" style="left:137px;top:1471px;width:392px;height:392px;background:linear-gradient(120deg,#2aa6a8,#5e6a5c 50%,#23282f)" role="img" aria-label="Portrait of Lena holding a teal umbrella"></div>
  <h2 class="heading" style="left:590px;top:1515px"><span class="heading-dot"></span>ABOUT LENA</h2>
  <div class="copy" style="left:590px;top:1606px;width:496px">
    <p>In my twenty years of work experience, people were always at the center of everything i did, honouring everyone's uniqueness and preferences. Understanding a person's ambitions gives me insights into the type of support, experiences, patnerships, and nurturing they need to thrive.</p>
    <p>My strength is to find insight into how each human being is unique and distinct from everyone else and open people's minds to new and wondrous possibilities.</p>
  </div>
  <a class="btn btn-blue" style="left:590px;top:1810px;width:181px" href="#">Connect With Us</a>

  <!-- Concierge -->
  <section class="concierge">
    <h2 class="heading center" style="top:98px;color:var(--white)"><span class="heading-dot"></span>CONCIERGE</h2>
    <p class="concierge-lead">Concierge Package offers you an ongoing partnership as you navigateyour journey to reach your full potential.</p>
    <div class="service" style="left:225px;top:254px"><div class="service-photo" style="background:linear-gradient(135deg,#c9a27a,#5a4634)" role="img" aria-label="Coach presenting to a small group in an office"></div>Coaching</div>
    <div class="service" style="left:495px;top:254px"><div class="service-photo" style="background:linear-gradient(135deg,#e7ecef,#8c99a3)" role="img" aria-label="Two people in a consulting meeting with a laptop"></div>Consulting</div>
    <div class="service" style="left:766px;top:254px"><div class="service-photo" style="background:linear-gradient(135deg,#d9b08c,#7a4b3a)" role="img" aria-label="Woman on a video chat at her laptop"></div>Fireside Chat</div>
    <svg class="abs" style="left:0;top:573px" width="1200" height="136" viewBox="0 0 1200 136"><path d="M0 136 C300 10 900 10 1200 136Z" fill="#fff"/></svg>
  </section>

  <!-- Rise Onward -->
  <h2 class="heading center" style="top:2679px"><span class="heading-dot"></span>RISE ONWARD</h2>
  <div class="plan" style="left:160px">
    <span class="plan-icon"></span>
    <h3>Rise Onward Light (Half day)</h3>
    <p class="plan-text">This is a fantastic oppourtunity to understand, WHY you carry the heavy backpack throughtout your life.</p>
    <ul><li><svg width="16" height="16" viewBox="0 0 16 16"><circle cx="8" cy="8" r="7" fill="none" stroke="#0a4fb0" stroke-width="1.3"/><path d="M4.5 8.2l2.3 2.2 4.7-4.8" fill="none" stroke="#0a4fb0" stroke-width="1.5"/></svg>Lorem Ipsum is simply dummy</li></ul>
    <a class="btn btn-blue" href="#">Join Now</a>
  </div>
  <div class="plan" style="left:463px">
    <span class="plan-icon"></span>
    <h3>Rise Onward (2-3 days)</h3>
    <p class="plan-text">We invite you to unpack your backpack, inspect the items you are carrying and decide WHAT to carry.</p>
    <ul>
      <li><svg width="16" height="16" viewBox="0 0 16 16"><circle cx="8" cy="8" r="7" fill="none" stroke="#0a4fb0" stroke-width="1.3"/><path d="M4.5 8.2l2.3 2.2 4.7-4.8" fill="none" stroke="#0a4fb0" stroke-width="1.5"/></svg>Lorem Ipsum is simply dummy</li>
      <li><svg width="16" height="16" viewBox="0 0 16 16"><circle cx="8" cy="8" r="7" fill="none" stroke="#0a4fb0" stroke-width="1.3"/><path d="M4.5 8.2l2.3 2.2 4.7-4.8" fill="none" stroke="#0a4fb0" stroke-width="1.5"/></svg>Lorem Ipsum is simply</li>
    </ul>
    <a class="btn btn-blue" href="#">Join Now</a>
  </div>
  <div class="plan" style="left:764px">
    <span class="plan-icon"></span>
    <h3>Rise Onward Unlimited (1 Week)</h3>
    <p class="plan-text">You design your new backpack and decide HOW you want to carry it through your life.</p>
    <ul>
      <li><svg width="16" height="16" viewBox="0 0 16 16"><circle cx="8" cy="8" r="7" fill="none" stroke="#0a4fb0" stroke-width="1.3"/><path d="M4.5 8.2l2.3 2.2 4.7-4.8" fill="none" stroke="#0a4fb0" stroke-width="1.5"/></svg>Lorem Ipsum is simply dummy</li>
      <li><svg width="16" height="16" viewBox="0 0 16 16"><circle cx="8" cy="8" r="7" fill="none" stroke="#0a4fb0" stroke-width="1.3"/><path d="M4.5 8.2l2.3 2.2 4.7-4.8" fill="none" stroke="#0a4fb0" stroke-width="1.5"/></svg>Lorem Ipsum is simply</li>
      <li><svg width="16" height="16" viewBox="0 0 16 16"><circle cx="8" cy="8" r="7" fill="none" stroke="#0a4fb0" stroke-width="1.3"/><path d="M4.5 8.2l2.3 2.2 4.7-4.8" fill="none" stroke="#0a4fb0" stroke-width="1.5"/></svg>Lorem Ipsum is simply dummy</li>
    </ul>
    <a class="btn btn-blue" href="#">Join Now</a>
  </div>

  <!-- Vantara Q+ -->
  <section class="plus">
    <svg class="abs" style="left:0;top:0" width="1200" height="140" viewBox="0 0 1200 140"><path d="M0 0 C300 150 900 150 1200 0 L1200 -1 L0 -1Z" fill="#fff"/></svg>
  </section>
  <h2 class="heading center" style="top:3388px"><span class="heading-dot" style="background:var(--ink)"></span>VANTARA Q+</h2>
  <div class="plus-card" style="left:114px">
    <div class="plus-photo" style="background:linear-gradient(160deg,#e6a35a,#6b5a48 60%,#2d3a2a)" role="img" aria-label="Camper van parked at sunset"></div>
    <h3>Coaching Insights</h3>
    <p>Become familiar with the insights and principles of coaching and understand their benefits.</p>
    <a class="btn btn-white" href="#">View More</a>
  </div>
  <div class="plus-card" style="left:444px">
    <div class="plus-photo" style="background:linear-gradient(180deg,#b9c7cf,#5f7a5a 55%,#3d5a35)" role="img" aria-label="Hiker with a backpack on a mountain trail"></div>
    <h3>Grab and go</h3>
    <p>Invitation to grap valuable tips to make a change in your life!</p>
    <a class="btn btn-white" href="#">View More</a>
  </div>
  <div class="plus-card" style="left:773px">
    <div class="plus-photo" style="background:linear-gradient(135deg,#c8d6e0,#e9d9c1 50%,#8a7e6c)" role="img" aria-label="Two travellers reading a map in a city street"></div>
    <h3>Be Resourcaful</h3>
    <p>Pay attention to the valuable resources which you can benefit from.</p>
    <a class="btn btn-white" href="#">View More</a>
  </div>

  <!-- Contact -->
  <h2 class="heading center" style="top:3986px"><span class="heading-dot" style="background:var(--ink)"></span>GET IN TOUCH WITH US</h2>
  <div class="contact-item" style="top:4143px">
    <svg width="20" height="24" viewBox="0 0 20 24"><path d="M10 0a8 8 0 0 0-8 8c0 6 8 16 8 16s8-10 8-16a8 8 0 0 0-8-8zm0 11a3 3 0 1 1 0-6 3 3 0 0 1 0 6z" fill="#0a4fb0"/></svg>
    <div><h4>Address</h4><p>Lorem ipsum dolor sit amet, consectetur adipis<br>cing elit, sed do eiusmod tempor</p></div>
  </div>
  <div class="contact-item" style="top:4222px">
    <svg width="22" height="16" viewBox="0 0 22 16"><rect width="22" height="16" rx="2" fill="#0a4fb0"/><path d="M1 2l10 7 10-7" fill="none" stroke="#fff" stroke-width="1.6"/></svg>
    <div><h4>Email Address</h4><p>hello@vantaraq.example<br>team@vantaraq.example</p></div>
  </div>
  <div class="contact-item" style="top:4301px">
    <svg width="20" height="20" viewBox="0 0 24 24"><path fill="#0a4fb0" d="M6.6 10.8a15.1 15.1 0 0 0 6.6 6.6l2.2-2.2a1 1 0 0 1 1-.25 11.4 11.4 0 0 0 3.6.57 1 1 0 0 1 1 1V20a1 1 0 0 1-1 1A17 17 0 0 1 3 4a1 1 0 0 1 1-1h3.5a1 1 0 0 1 1 1c0 1.25.2 2.45.57 3.57a1 1 0 0 1-.25 1z"/></svg>
    <div><h4>Phone Number</h4><p>+1 555 014 2290<br>(555) 7731-0468</p></div>
  </div>
  <form class="form-box">
    <div class="field" style="left:44px;top:50px;width:210px">Your Name</div>
    <div class="field" style="left:282px;top:50px;width:210px">Email Address</div>
    <div class="field" style="left:44px;top:106px;width:210px">Phone Number</div>
    <div class="field" style="left:282px;top:106px;width:210px">Subject</div>
    <div class="field" style="left:44px;top:162px;width:448px;height:50px">Your Message Goes Here</div>
    <a class="btn btn-blue btn-submit" href="#">Submit</a>
  </form>

  <!-- Footer -->
  <svg class="abs" style="left:0;top:4470px" width="1200" height="440" viewBox="0 0 1200 440">
    <path d="M0 190 C300 60 700 20 1200 0 L1200 440 L0 440Z" fill="var(--yellow)"/>
    <path d="M0 198 C300 68 700 28 1200 10 L1200 440 L0 440Z" fill="var(--blue)"/>
    <path d="M0 206 C300 76 700 36 1200 20 L1200 440 L0 440Z" fill="#000"/>
  </svg>
  <a class="brand" style="left:0;width:1200px;justify-content:center;top:4632px;color:var(--yellow);font-size:16px" href="#"><span class="brand-dot"></span>VANTARA Q</a>
  <nav class="footer-nav">
    <a href="#">HOME</a><a href="#">ABOUT US</a><a href="#">O.R.B.</a><a href="#">CONCIERGE</a><a href="#">RISE ONWARD</a><a href="#">VANTARA Q+</a><a href="#">TESTIMONIALS</a>
  </nav>
  <div class="footer-rule"></div>
  <p class="copyright">Copyright 2022 © Vantara Q | All Rights Reserved.</p>
  <div class="socials" aria-label="Social links"><span></span><span></span><span></span><span></span></div>

</div>
</body>
</html>
```